Corvale Homes

To produce a business card design for our newly established house building and development company, We have had a logo design done please see attached, our slogan is "building your home sweet home"
Contact Information for Business Card
Adress on card needs to Read - 58 Elmsworth Lane, Kettering, Northamptonshire NN16 4QT. Director name Dean Vascotti
Requirements
Must have
- Web adress is www.corvale-homes.co.uk
- Email address is info@corvale-homes.co.uk
- phone number 07700 900417

```html
<!DOCTYPE html>
<html lang="en">
<head>
<meta charset="utf-8">
<title>Corvale Homes — Business Card</title>
<link rel="stylesheet" href="https://fonts.googleapis.com/css2?family=Arimo:wght@400;700&family=Source+Sans+3:wght@400&display=swap">
<style>
  :root {
    --page: #f8f9fa;
    --card: #fbfbfa;
    --green: #8cc63f;
    --grey: #999999;
  }
  * { margin: 0; padding: 0; box-sizing: border-box; }
  html, body {
    width: 1200px; height: 1200px; overflow: hidden;
    background: var(--page);
  }
  .canvas { position: relative; width: 1200px; height: 1200px; }
  .card {
    position: absolute; left: 193px; width: 840px; height: 480px;
    background: var(--card); overflow: hidden;
  }
  .card--front { top: 90px; }
  .card--back { top: 600px; }
  .roof { position: absolute; left: 0; top: 0; width: 840px; height: 480px; }
  .roof .band { fill: var(--green); }
  .roof .ridge { fill: var(--grey); }

  .brand {
    position: absolute; left: 0; right: 0; top: 296px;
    text-align: center; color: var(--green);
    font-family: "Arimo", Arial, sans-serif;
  }
  .brand__name {
    font-weight: 700; font-size: 56px; letter-spacing: 1px; line-height: 1;
  }

  .info { position: absolute; color: var(--green); }
  .info::before {
    content: ""; position: absolute; left: -21px; top: 2px; bottom: 2px;
    width: 9px; border-radius: 5px; background: var(--green);
  }
  .info--person { left: 81px; top: 146px; }
  .info--contact { left: 381px; top: 342px; }
  .person__name {
    font-family: "Arimo", Arial, sans-serif; font-weight: 700;
    font-size: 30px; line-height: 40px;
  }
  .person__role {
    font-family: "Arimo", Arial, sans-serif; font-weight: 400;
    font-size: 30px; line-height: 40px; letter-spacing: -0.5px;
  }
  .person__address {
    font-family: "Source Sans 3", "Myriad Pro", sans-serif;
    font-size: 30px; line-height: 41px; font-style: normal;
  }
  .contact__line {
    display: block; font-family: "Arimo", Arial, sans-serif; font-weight: 700;
    font-size: 26.5px; line-height: 37px; color: var(--green); text-decoration: none;
  }
</style>
</head>
<body>
<main class="canvas">
  <section class="card card--front">
    <svg class="roof" viewBox="0 0 1050 600" aria-hidden="true">
      <polygon class="band" points="0,0 1050,0 1050,285 405,37 0,174"/>
      <polygon class="ridge" points="0,174 405,37 1050,285 1050,311 405,63 0,200"/>
    </svg>
    <div class="brand">
      <div class="brand__name">CORVALE HOMES</div>
    </div>
  </section>

  <section class="card card--back">
    <svg class="roof" viewBox="0 0 1050 600" aria-hidden="true">
      <polygon class="band" points="0,0 1050,0 1050,283 405,37 0,173"/>
      <polygon class="ridge" points="0,173 405,37 1050,283 1050,310 405,63 0,200"/>
    </svg>
    <div class="info info--person">
      <div class="person__name">Dean Vascotti</div>
      <div class="person__role">Director</div>
      <address class="person__address">58 Elmsworth Lane, Kettering,<br>Northamptonshire NN16 4QT.</address>
    </div>
    <div class="info info--contact">
      <a class="contact__line" href="#">www.corvale-homes.co.uk</a>
      <a class="contact__line" href="#">info@corvale-homes.co.uk</a>
      <a class="contact__line" href="#">07700 900417</a>
    </div>
  </section>
</main>
</body>
</html>
```